We are looking for an effective ad to recruit work from home Loan Officers for our Mortgage Brokerage.
Use the following text...
Earn Mortgage Income in your sleep. Its as easy as 1, 2, 3.....
1) Solicit Potential Applicants (Word of Mouth, Email, Social Media etc.)
2) Take Complete Applications & Submit Them
3) Wait to Get Paid.......(Avg. $2,500 per closing)
"You open the door, we'll finish the deal"
No Experience Necessary
No Goals or Quotas
No Office Hours / Work from Home Office
...and We Fully Reimburse ALL LICENSING FEES!!
Email Resume to mwelby@brightharborloans.example
Bright Harbor Lending Group, Inc.
947 W Caldwell Avenue, #318
Baltimore, MD 21230
NMLS #731860
www.brightharborloans.example
Phone (800) 555-0142
Licensed Mortgage Broker in MD and DC since 1997
Target Market(s)
Professionals looking to earn part time income at Loan Officers, preferably with strong social media following.
Industry/Entity Type
Loan
Look and feel

```html
<!DOCTYPE html>
<html lang="en">
<head>
<meta charset="utf-8">
<title>Bright Harbor Lending Group – Loan Officer Recruitment Flyer</title>
<link href="https://fonts.googleapis.com/css2?family=Oswald:wght@500;700&family=Open+Sans:wght@300;400&family=Montserrat:wght@700&family=Dosis:wght@500;600&display=swap" rel="stylesheet">
<style>
  :root {
    --page-bg: #e9e9ea;
    --navy-deep: #0a3a86;
    --navy: #0d4aa6;
    --navy-light: #1f6ac4;
    --gold: #b5a22a;
    --yellow-text: #f4c51c;
    --white: #ffffff;
    --ink-blue: #1551a8;
  }
  * { box-sizing: border-box; margin: 0; padding: 0; }
  html, body { width: 1200px; height: 1200px; overflow: hidden; background: var(--page-bg); }
  .canvas { position: relative; width: 1200px; height: 1200px; }
  .flyer {
    position: absolute; left: 160px; top: 30px;
    width: 820px; height: 1062px;
    transform: scale(1.0734); transform-origin: top left;
    background: radial-gradient(ellipse at 55% 55%, var(--navy-light) 0%, var(--navy) 45%, var(--navy-deep) 100%);
    color: var(--white); overflow: hidden;
  }
  .tagline-top {
    position: absolute; left: 70px; top: 27px; width: 418px;
    font: 400 16px/1 "Open Sans", sans-serif; text-align: center; white-space: nowrap; letter-spacing: -0.2px;
  }
  .headline {
    position: absolute; left: 68px; top: 50px; width: 420px; height: 280px;
    filter: drop-shadow(3px 3px 3px rgba(0,0,0,.45));
  }
  .headline text {
    font-family: "Oswald", sans-serif; font-weight: 700; fill: var(--white); text-transform: uppercase;
  }
  .brand-box {
    position: absolute; left: 518px; top: 0; width: 280px; height: 318px;
    background: var(--white); display: flex; align-items: center; justify-content: center; gap: 10px;
    padding: 0 18px;
  }
  .brand-box .mark { flex: none; width: 34px; height: 34px; border-radius: 50%; background: var(--gold); }
  .brand-box .name { font: 500 22px/1.15 "Oswald", sans-serif; color: var(--ink-blue); text-transform: uppercase; }
  .easy-band {
    position: absolute; left: 0; top: 350px; width: 820px; height: 36px;
    background: linear-gradient(90deg, var(--gold) 0%, var(--gold) 22%, #3f6a8a 42%, #3f6a8a 58%, var(--gold) 78%, var(--gold) 100%);
  }
  .easy-band p {
    position: absolute; left: 0; right: 0; top: -5px; text-align: center; padding-left: 20px;
    font: 700 38px/1 "Oswald", sans-serif; color: var(--yellow-text); letter-spacing: -0.5px; white-space: nowrap;
    text-shadow: 1px 1px 2px rgba(0,0,0,.35);
  }
  .steps { position: absolute; left: 95px; top: 420px; list-style: none; }
  .step { position: absolute; left: 0; display: flex; align-items: center; width: 690px; }
  .step .num {
    flex: none; width: 80px; height: 80px; border-radius: 50%;
    background: radial-gradient(circle at 40% 30%, #ffd84a 0%, #f0a10e 55%, #c97705 100%);
    box-shadow: 0 3px 6px rgba(0,0,0,.35);
    display: flex; align-items: center; justify-content: center;
    font: 700 50px/1 "Oswald", sans-serif; color: var(--white); text-shadow: 2px 2px 3px rgba(0,0,0,.45);
  }
  .step .text { margin-left: 18px; font: 300 24px/30px "Open Sans", sans-serif; text-transform: uppercase; white-space: nowrap; }
  .step-1 { top: 0; } .step-2 { top: 90px; } .step-3 { top: 185px; }
  .social-badge {
    position: absolute; left: 90px; top: 722px; width: 358px; height: 106px;
    background: var(--white); border-radius: 8px; border: 3px solid #c9d3e6;
    box-shadow: 0 3px 8px rgba(0,0,0,.4);
    display: flex; align-items: center; gap: 16px; padding: 0 20px;
  }
  .social-badge .square { flex: none; width: 70px; height: 70px; border-radius: 8px; background: var(--ink-blue); }
  .social-badge .label { font: 700 30px/1.05 "Montserrat", sans-serif; color: var(--ink-blue); }
  .social-badge .label small { display: block; font-size: 18px; }
  .perks { position: absolute; left: 476px; top: 720px; list-style: none;
    font: 500 19px/1.25 "Dosis", sans-serif; color: var(--yellow-text); text-transform: uppercase; }
  .perks li { margin-bottom: 9px; padding-left: 10px; text-indent: -10px; white-space: nowrap; }
  .perks li::before { content: "• "; }
  .reimburse { position: absolute; left: 0; right: 0; top: 858px; text-align: center;
    font: 700 18px/1 "Montserrat", sans-serif; letter-spacing: 1px; white-space: nowrap; }
  .motto { position: absolute; left: 0; right: 0; top: 888px; text-align: center;
    font: 700 33px/1 "Oswald", sans-serif; color: var(--yellow-text); text-transform: uppercase; white-space: nowrap;
    letter-spacing: -0.5px; text-shadow: 1px 1px 2px rgba(0,0,0,.35); }
  .footer { position: absolute; left: 0; top: 945px; width: 820px; height: 117px; background: var(--gold); }
  .footer .icon { position: absolute; }
  .footer p { white-space: nowrap; }
  .address { position: absolute; left: 98px; top: 17px; font: 500 14.5px/19.5px "Dosis", sans-serif; }
  .phone { position: absolute; left: 383px; top: 14px; font: 500 30px/1 "Dosis", sans-serif; }
  .email { position: absolute; left: 383px; top: 69px; font: 500 12.5px/1 "Dosis", sans-serif; }
  .web { position: absolute; left: 624px; top: 69px; font: 500 12.5px/1 "Dosis", sans-serif; }
</style>
</head>
<body>
<div class="canvas">
  <article class="flyer">
    <p class="tagline-top">Licensed Mortgage Broker in MD and DC since 1997</p>
    <svg class="headline" viewBox="0 0 420 280" role="heading" aria-level="1" aria-label="Earn Mortgage Income In Your Sleep">
      <text x="2" y="60" font-size="70" textLength="416" lengthAdjust="spacingAndGlyphs">EARN MORTGAGE</text>
      <text x="2" y="190" font-size="146" textLength="416" lengthAdjust="spacingAndGlyphs">INCOME</text>
      <text x="2" y="270" font-size="84" textLength="416" lengthAdjust="spacingAndGlyphs">IN YOUR SLEEP</text>
    </svg>

    <div class="brand-box">
      <span class="mark"></span>
      <span class="name">Bright Harbor Lending Group, Inc.</span>
    </div>

    <div class="easy-band"><p>It’s As EASY As 1, 2, 3.....</p></div>

    <ol class="steps">
      <li class="step step-1"><span class="num">1</span><span class="text">Solicit potential applicants<br>(word of mouth, email, social media etc.)</span></li>
      <li class="step step-2"><span class="num">2</span><span class="text">Take complete applications &amp;<br>submit them</span></li>
      <li class="step step-3"><span class="num">3</span><span class="text">Wait to get paid (avg. $2,500 per closing)</span></li>
    </ol>

    <div class="social-badge">
      <span class="square"></span>
      <span class="label"><small>LIKE US ON</small>neighborly</span>
    </div>

    <ul class="perks">
      <li>No experience necessary</li>
      <li>No goals or quotas</li>
      <li>No office hours / work<br>from home office</li>
    </ul>

    <p class="reimburse">...AND WE FULLY REIMBURSE ALL LICENSING FEES!!</p>
    <p class="motto">"You open the door, we'll finish the deal"</p>

    <footer class="footer">
      <svg class="icon" style="left:34px;top:14px" width="48" height="76" viewBox="0 0 48 76" aria-hidden="true">
        <path d="M24 2C12 2 3 11 3 23c0 16 21 38 21 38s21-22 21-38C45 11 36 2 24 2z" fill="#fff"/>
        <circle cx="24" cy="23" r="9" fill="#b5a22a"/>
        <ellipse cx="24" cy="70" rx="14" ry="3" fill="none" stroke="#fff" stroke-width="2"/>
      </svg>
      <p class="address">Bright Harbor Lending Group, Inc.<br>947 W Caldwell Avenue, #318<br>Baltimore, MD 21230<br>NMLS #731860</p>

      <svg class="icon" style="left:334px;top:10px" width="42" height="42" viewBox="0 0 42 42" aria-hidden="true">
        <circle cx="21" cy="21" r="19" fill="none" stroke="#fff" stroke-width="2.5"/>
        <path d="M14 11l5 5-3 3c1.5 3 4 5.5 7 7l3-3 5 5-3 3c-8-1-16-9-17-17z" fill="#fff"/>
      </svg>
      <p class="phone">(800) 555-0142</p>

      <svg class="icon" style="left:339px;top:65px" width="34" height="22" viewBox="0 0 34 22" aria-hidden="true">
        <rect x="1.5" y="1.5" width="31" height="19" fill="none" stroke="#fff" stroke-width="2.5"/>
        <path d="M2 2l15 11L32 2M2 20l11-9M32 20l-11-9" fill="none" stroke="#fff" stroke-width="2.5"/>
      </svg>
      <p class="email">mwelby@brightharborloans.example</p>

      <svg class="icon" style="left:592px;top:63px" width="26" height="26" viewBox="0 0 30 30" aria-hidden="true">
        <circle cx="15" cy="15" r="13" fill="none" stroke="#fff" stroke-width="2.2"/>
        <ellipse cx="15" cy="15" rx="6" ry="13" fill="none" stroke="#fff" stroke-width="2"/>
        <path d="M2 15h26M4 8h22M4 22h22" stroke="#fff" stroke-width="2"/>
      </svg>
      <p class="web">www.brightharborloans.example</p>
    </footer>
  </article>
</div>
</body>
</html>
```